Bureau for Venture and Discovery Needs a Graphically Designed Powerpoint Template

We are from Bureau for Venture and Discovery (BVaD), part of a medical school. BVaD contributes to the medical school by overseeing and managing intellectual property generated by researchers at the medical school, and also works to ensure optimal commercial outcomes for all inventions arising from the medical school. We want a graphically designed powerpoint presentation template to describe how BVaD is involved in a researcher’s journey to major scientific contributions. The journey should be represented in the form of a main road (or pathway). Along the main road, there will be smaller roads branching out, each representing one of the researcher’s major scientific contributions. We will be inputting text details of each major scientific contribution near each of the small road branches. The smaller road branches will also need to be removable / editable. This is because we might need to send the template to different researchers to input details of their major scientific contributions, and each researcher will have a different number of them. Hence, you can possibly place around 6 branches along the main road, but we want to be able to remove the branches should we need to. Removal of the branches (design elements) should still result in a seamless image in powerpoint. We also want to be able to add and edit text in the design template. The start of the main road should contain a placeholder for us to place the researcher’s photo. The end of the road will lead to one of the major scientific contributions. Please see the uploaded sketch to have an idea of what we are looking to get. We welcome deviations and changes to the design as shown from the sketch, as long as the design is able to convey what we have described above. As this powerpoint template will be used for presentation to the senior management, we need it to look beautiful yet professional.

Target Market(s)

Researcher, Scientist

Industry/Entity Type

School

Font styles to use
Serif
Sans Serif

Requirements
Must have
• A main road or pathway as mentioned in the project description.
Nice to have
• We will leave the "nice to haves" to be decided by the designer.
Should not have
• Trees

```html
<!DOCTYPE html>
<html lang="en">
<head>
<meta charset="utf-8">
<title>BVaD services / a researcher's journey</title>
<link href="https://fonts.googleapis.com/css2?family=Playfair+Display:wght@400;700;800&family=Arimo:wght@400;700&display=swap" rel="stylesheet">
<style>
  :root {
    --ink: #1a1a1a;
    --text-grey: #555a60;
    --blue-deep: #1b5fa6;
    --blue-mid: #2b8ccf;
    --blue-light: #3298d6;
    --teal: #2bb5a0;
    --teal-blue: #2378aa;
    --marker: #3a3a3a;
    --white: #ffffff;
    --bg-top: #ffffff;
    --bg-bottom: #eeeeef;
  }
  * { box-sizing: border-box; margin: 0; padding: 0; }
  html, body { width: 1200px; height: 675px; overflow: hidden; }
  body { background: var(--white); }
  .slide {
    position: relative;
    width: 1200px;
    height: 675px;
    overflow: hidden;
    background: radial-gradient(ellipse at 20% 20%, var(--bg-top) 30%, var(--bg-bottom) 100%);
    font-family: "Arimo", Arial, sans-serif;
  }
  .slide-title {
    position: absolute;
    left: 56px;
    top: 54px;
    font-family: "Playfair Display", Georgia, serif;
    font-weight: 400;
    font-size: 46px;
    line-height: 56px;
    color: var(--ink);
  }
  .slide-title .subtitle {
    display: block;
    font-weight: 700;
    background: linear-gradient(90deg, var(--blue-deep) 0%, var(--blue-mid) 45%, var(--teal) 100%);
    -webkit-background-clip: text;
    background-clip: text;
    color: transparent;
  }
  .slide-title .slash { font-weight: 400; }

  .profile-card {
    position: absolute;
    left: 54px;
    top: 183px;
    width: 162px;
    height: 424px;
    background: var(--white);
    border-radius: 0 0 10px 0;
    box-shadow: 3px 3px 6px rgba(0,0,0,0.22);
    z-index: 2;
  }
  .profile-photo {
    position: absolute;
    left: 17px;
    top: 16px;
    width: 127px;
    height: 126px;
    background: linear-gradient(135deg, #c9d4da 0%, #d98a72 45%, #f2e6e0 100%);
  }
  .researcher-name {
    position: absolute;
    left: 17px;
    top: 153px;
    font-family: "Playfair Display", Georgia, serif;
    font-weight: 700;
    font-size: 17px;
    line-height: 22px;
    color: #333;
  }
  .profile-rule {
    position: absolute;
    left: 17px;
    width: 32px;
    border-top: 2px solid #333;
  }
  .profile-label {
    position: absolute;
    left: 17px;
    font-weight: 700;
    font-size: 12px;
    color: #333;
  }
  .profile-value {
    position: absolute;
    left: 17px;
    font-size: 12px;
    color: var(--text-grey);
  }
  .subject-list {
    position: absolute;
    left: 17px;
    top: 302px;
    list-style: none;
    font-size: 12px;
    line-height: 15px;
    color: var(--text-grey);
  }
  .subject-list li::before { content: "•"; display: inline-block; width: 29px; color: #333; }

  .journey { position: absolute; left: 0; top: 0; z-index: 1; }

  .milestone {
    position: absolute;
    width: 176px;
    height: 172px;
    padding: 16px 14px;
    border-radius: 4px;
    color: var(--white);
    background: linear-gradient(160deg, var(--blue-light) 0%, var(--blue-deep) 100%);
    box-shadow: 3px 4px 6px rgba(0,0,0,0.22);
    z-index: 3;
  }
  .milestone.project {
    background: linear-gradient(160deg, var(--teal-blue) 0%, var(--teal) 100%);
    width: 184px;
    height: 170px;
  }
  .milestone-title {
    font-family: "Playfair Display", Georgia, serif;
    font-weight: 700;
    font-size: 12.5px;
    line-height: 15px;
    margin-bottom: 16px;
  }
  .milestone-text {
    font-size: 12px;
    line-height: 15px;
  }
  .milestone-icon {
    position: absolute;
    right: 12px;
    bottom: 10px;
    width: 26px;
    height: 26px;
  }
</style>
</head>
<body>
<div class="slide">

  <h1 class="slide-title">BVaD services
    <span class="subtitle"><span class="slash">/ </span>a researcher’s journey</span>
  </h1>

  <svg class="journey" width="1200" height="675" viewBox="0 0 1200 675" aria-hidden="true">
    <defs>
      <linearGradient id="roadGradient" x1="0" y1="190" x2="0" y2="600" gradientUnits="userSpaceOnUse">
        <stop offset="0" stop-color="#1b63a5"/>
        <stop offset="1" stop-color="#2bb0a0"/>
      </linearGradient>
    </defs>
    <path d="M216 279 C255 215 295 191 335 191 C405 191 470 300 535 392 C605 492 680 596 755 596 C840 596 925 535 985 478 C1055 410 1100 355 1146 321"
          fill="none" stroke="url(#roadGradient)" stroke-width="2"/>
    <g stroke="var(--marker)" stroke-width="1">
      <line x1="265" y1="221" x2="265" y2="263"/>
      <line x1="535" y1="392" x2="535" y2="352"/>
      <line x1="693" y1="579" x2="693" y2="540"/>
      <line x1="948" y1="493" x2="948" y2="455"/>
    </g>
    <g fill="none" stroke="var(--marker)" stroke-width="1">
      <circle cx="265" cy="221" r="10"/><circle cx="265" cy="221" r="7"/>
      <circle cx="535" cy="392" r="10"/><circle cx="535" cy="392" r="7"/>
      <circle cx="693" cy="579" r="10"/><circle cx="693" cy="579" r="7"/>
      <circle cx="948" cy="493" r="10"/><circle cx="948" cy="493" r="7"/>
    </g>
    <g fill="var(--marker)">
      <circle cx="265" cy="221" r="4"/>
      <circle cx="535" cy="392" r="4"/>
      <circle cx="693" cy="579" r="4"/>
      <circle cx="948" cy="493" r="4"/>
    </g>
  </svg>

  <aside class="profile-card">
    <div class="profile-photo" role="img" aria-label="Researcher portrait photo placeholder"></div>
    <h2 class="researcher-name">Researcher’s<br>name PhD.</h2>
    <div class="profile-rule" style="top:222px"></div>
    <div class="profile-label" style="top:227px">Institution</div>
    <div class="profile-value" style="top:243px">Lorem ipsum</div>
    <div class="profile-rule" style="top:282px"></div>
    <div class="profile-label" style="top:287px">Research subjects</div>
    <ul class="subject-list" style="top:303px">
      <li>Lorem ipsum</li>
      <li>Lorem ipsum</li>
      <li>Lorem ipsum</li>
    </ul>
  </aside>

  <section class="milestone project" style="left:254px; top:263px;">
    <h3 class="milestone-title">BVaD xyz<br>Project</h3>
    <p class="milestone-text">Lorem ipsum dolor sit amet, consectetur adipiscing elit. Ut ornare nunc nec lectus aliquam, eget accumsan felis fermentum.</p>
    <svg class="milestone-icon" viewBox="0 0 26 26" aria-hidden="true">
      <path d="M24 2 L2 11 L11 14 L14 24 Z M24 2 L11 14" fill="none" stroke="#fff" stroke-width="1.2" stroke-linejoin="round"/>
    </svg>
  </section>

  <section class="milestone" style="left:525px; top:181px;">
    <h3 class="milestone-title">Major scientific<br>constribution</h3>
    <p class="milestone-text">Lorem ipsum dolor sit amet, consectetur adipiscing elit. Ut ornare nunc nec lectus aliquam, eget accumsan felis fermentum.</p>
    <svg class="milestone-icon" viewBox="0 0 26 26" aria-hidden="true">
      <path d="M4 25 V2 M4 4 H16 L14 7 H23 L20 11 L23 15 H11 L13 11 H4" fill="none" stroke="#fff" stroke-width="1.2" stroke-linejoin="round"/>
    </svg>
  </section>

  <section class="milestone" style="left:683px; top:368px;">
    <h3 class="milestone-title">Major scientific<br>constribution</h3>
    <p class="milestone-text">Lorem ipsum dolor sit amet, consectetur adipiscing elit. Ut ornare nunc nec lectus aliquam, eget accumsan felis fermentum.</p>
    <svg class="milestone-icon" viewBox="0 0 26 26" aria-hidden="true">
      <path d="M4 25 V2 M4 4 H16 L14 7 H23 L20 11 L23 15 H11 L13 11 H4" fill="none" stroke="#fff" stroke-width="1.2" stroke-linejoin="round"/>
    </svg>
  </section>

  <section class="milestone" style="left:937px; top:283px;">
    <h3 class="milestone-title">Major scientific<br>constribution</h3>
    <p class="milestone-text">Lorem ipsum dolor sit amet, consectetur adipiscing elit. Ut ornare nunc nec lectus aliquam, eget accumsan felis fermentum.</p>
    <svg class="milestone-icon" viewBox="0 0 26 26" aria-hidden="true">
      <path d="M4 25 V2 M4 4 H16 L14 7 H23 L20 11 L23 15 H11 L13 11 H4" fill="none" stroke="#fff" stroke-width="1.2" stroke-linejoin="round"/>
    </svg>
  </section>

</div>
</body>
</html>
```